Tulven Electrics Flyer Design Advertising

I am after an A5 Flyer design to help promote my electrical services business.
I would like to have information on what my business offers, photos of electrical work, and specials/deals for an amount of time.

Industry/Entity Type

Electrician

Font styles to use
Sans Serif

Colors
0292cd
33a6d7
85cae6
3176b5
333333
1b1b1b
ffffff
5c5c5c
474747

Requirements
Must have
• Specialising in New homes, renovations and commercial projects
• Contact details:
• ph. 0437 619 458
• email admin@tulvenelectrics.example.au
• facebook TulvenElectrics
• Specials/Deals:
• 10% off all electrical services
• or
• Free LED downlights on installation
• *Terms conditions apply
• ALL RESIDENTIAL & COMMERCIAL ELECTRICAL SERVICES
• - New Home installations
• - Commercial projects
• - Shop fit outs
• - Renovations
• - Smoke Detectors
• - Air Conditioning and Ceiling Fans
• - Garden Lighting
• - Oven and Cooktop Installations
• - Power Point installation
• - LED lighting upgrades
• - Security Lighting
• - Switchboard upgrades
• - Test and Tag
• - Commercial Property
• - General Electrical Maintenance

```html
<!DOCTYPE html>
<html lang="en">
<head>
<meta charset="utf-8">
<title>Tulven Electrics Flyer</title>
<link rel="stylesheet" href="https://fonts.googleapis.com/css2?family=Russo+One&family=Mukta:wght@400;500;700&display=swap">
<style>
  :root {
    --blue: #0292cd;
    --blue-mid: #33a6d7;
    --blue-light: #85cae6;
    --blue-deep: #3176b5;
    --ink: #333333;
    --ink-dark: #1b1b1b;
    --white: #ffffff;
    --grey: #5c5c5c;
    --grey-dark: #474747;
  }
  * { box-sizing: border-box; margin: 0; padding: 0; }
  html, body { width: 848px; height: 1200px; overflow: hidden; background: var(--white); }
  .flyer { position: relative; width: 848px; height: 1200px; overflow: hidden; font-family: "Mukta", sans-serif; }
  .backdrop { position: absolute; inset: 0; }

  .brand { position: absolute; left: 44px; top: 50px; display: flex; align-items: center; gap: 18px; }
  .brand-disc { width: 140px; height: 140px; border-radius: 50%; background: var(--blue); border: 6px solid var(--ink); }
  .brand-name { font-family: "Russo One", sans-serif; font-size: 36px; color: var(--ink); line-height: 1; }

  .contact { position: absolute; left: 70px; top: 202px; list-style: none; }
  .contact li { display: flex; align-items: center; gap: 10px; height: 26px; font-size: 16px; line-height: 1; color: var(--ink); }
  .contact svg { width: 17px; height: 17px; flex: none; }

  .tagline { position: absolute; left: 42px; top: 336px; width: 820px; transform-origin: 0 0; transform: rotate(-12deg);
    font-weight: 700; font-size: 17px; line-height: 20px; letter-spacing: 1.2px; color: var(--white); white-space: nowrap; }

  .photo { position: absolute; border: 3px solid var(--white); box-shadow: 0 2px 6px rgba(0,0,0,.3); }
  .photo-kitchen { left: 22px; top: 382px; width: 264px; height: 177px; background: linear-gradient(135deg, #f1f3f4, #c9d2d4 55%, #6f8a6a); }
  .photo-patio { left: 295px; top: 382px; width: 264px; height: 177px; background: linear-gradient(160deg, #9fb3b8, #4f6a3e 50%, #2f3a24); }
  .photo-pool { left: 569px; top: 382px; width: 260px; height: 177px; background: linear-gradient(180deg, #5fa9d8, #4f8a44 50%, #2fa3c9); }
  .photo-night { left: 570px; top: 586px; width: 259px; height: 192px; background: linear-gradient(180deg, #5a6d86, #b08a5a 55%, #2e5a3a); }

  .services-title { position: absolute; left: 44px; top: 588px; font-family: "Russo One", sans-serif; font-weight: 400; font-size: 25px; line-height: 34px;
    color: var(--white);
    text-shadow: -2px 0 var(--ink), 2px 0 var(--ink), 0 -2px var(--ink), 0 2px var(--ink), -1.5px -1.5px var(--ink), 1.5px 1.5px var(--ink), -1.5px 1.5px var(--ink), 1.5px -1.5px var(--ink); }
  .services { position: absolute; left: 56px; top: 680px; list-style: none; }
  .services li { position: relative; padding-left: 20px; height: 28.2px; font-size: 20px; line-height: 28px; color: var(--white); font-weight: 500; letter-spacing: .3px; }
  .services li::before { content: ""; position: absolute; left: 0; top: 12px; width: 5px; height: 5px; border-radius: 50%; background: var(--white); }

  .deals { position: absolute; left: 582px; top: 818px; width: 212px; height: 236px; background: var(--grey-dark); padding: 10px; }
  .deals-panel { width: 100%; height: 100%; background: linear-gradient(180deg, #e4e4e4, #c9c9c9); border: 2px solid var(--ink);
    display: flex; flex-direction: column; align-items: center; justify-content: center; text-align: center; color: var(--ink-dark); }
  .deal-big { font-family: "Russo One", sans-serif; font-size: 32px; line-height: 1; }
  .deal-free { font-size: 27px; }
  .deal-small { font-weight: 700; font-size: 12px; letter-spacing: .4px; margin-top: 2px; }
  .deal-or { font-size: 12px; color: var(--grey); margin: 6px 0 4px; }
  .deal-mid { font-weight: 700; font-size: 20px; line-height: 1.05; }
  .deal-terms { font-size: 10px; color: var(--grey); margin-top: 6px; }
  .deals-ribbon { position: absolute; right: -26px; top: 18px; width: 110px; height: 22px; transform: rotate(45deg);
    background: var(--white); border: 2px solid var(--grey-dark); font-weight: 700; font-size: 14px; line-height: 18px;
    text-align: center; color: var(--ink); letter-spacing: 1px; }

  .offer-ends { position: absolute; left: 522px; top: 1136px; font-size: 21px; line-height: 30px; color: var(--ink); }
  .offer-date { position: absolute; left: 658px; top: 1134px; width: 152px; height: 32px; background: var(--white); border: 1px solid #ddd; }
</style>
</head>
<body>
<main class="flyer">
  <svg class="backdrop" width="848" height="1200" viewBox="0 0 848 1200">
    <defs>
      <linearGradient id="room" x1="0" y1="0" x2="1" y2="1">
        <stop offset="0" stop-color="#f2f4f6"/>
        <stop offset=".6" stop-color="#dfe6ea"/>
        <stop offset="1" stop-color="#b9c7cf"/>
      </linearGradient>
      <linearGradient id="sea" x1="0" y1="0" x2="0" y2="1">
        <stop offset="0" stop-color="#85cae6"/>
        <stop offset=".25" stop-color="#33a6d7"/>
        <stop offset="1" stop-color="#0292cd"/>
      </linearGradient>
    </defs>
    <rect width="848" height="390" fill="url(#room)" role="img" aria-label="Photo of a bright interior with pendant lights"/>
    <polygon points="0,366 848,186 848,1200 0,1200" fill="url(#sea)"/>
    <polygon points="0,332 848,152 848,190 0,370" fill="var(--ink)"/>
    <polygon points="0,1168 848,1078 848,1200 0,1200" fill="#e9e9e9"/>
    <polygon points="0,1160 848,1070 848,1086 0,1176" fill="var(--ink)"/>
  </svg>

  <header class="brand">
    <div class="brand-disc"></div>
    <div class="brand-name">Tulven Electrics</div>
  </header>

  <ul class="contact">
    <li><svg viewBox="0 0 20 20"><circle cx="10" cy="10" r="9" fill="var(--blue)"/><path d="M1 10h18M10 1v18M4 4.5c4 2 8 2 12 0M4 15.5c4-2 8-2 12 0" stroke="#fff" stroke-width="1.2" fill="none"/></svg>admin@tulvenelectrics.example.au</li>
    <li><svg viewBox="0 0 20 20"><rect x="2" y="8" width="16" height="10" rx="2" fill="var(--blue)"/><path d="M2 8c0-5 16-5 16 0" stroke="var(--blue)" stroke-width="3" fill="none"/></svg>0437 619 458</li>
    <li><svg viewBox="0 0 20 20"><rect x="1" y="1" width="18" height="18" rx="3" fill="var(--blue-deep)"/></svg>/TulvenElectrics</li>
  </ul>

  <div class="tagline">SPECIALISING IN NEW HOMES, RENOVATIONS AND COMMERCIAL PROJECTS</div>

  <div class="photo photo-kitchen" role="img" aria-label="Photo of a modern kitchen with pendant lighting"></div>
  <div class="photo photo-patio" role="img" aria-label="Photo of a lit outdoor patio with garden"></div>
  <div class="photo photo-pool" role="img" aria-label="Photo of a pool with tropical garden"></div>
  <div class="photo photo-night" role="img" aria-label="Photo of a home and pool lit at dusk"></div>

  <h1 class="services-title">ALL RESIDENTIAL &amp; COMMERCIAL<br>ELECTRICAL SERVICES</h1>
  <ul class="services">
    <li>NEW HOME INSTALLATIONS</li>
    <li>COMMERCIAL PROJECTS</li>
    <li>SHOP FIT OUTS</li>
    <li>RENOVATIONS</li>
    <li>SMOKE DETECTORS</li>
    <li>AIR CONDITIONING AND CEILING FANS</li>
    <li>GARDEN LIGHTING</li>
    <li>OVEN AND COOKTOP INSTALLATIONS</li>
    <li>POWER POINT INSTALLATION</li>
    <li>LED LIGHTING UPGRADES</li>
    <li>SECURITY LIGHTING</li>
    <li>SWITCHBOARD UPGRADES</li>
    <li>TEST AND TAG</li>
    <li>COMMERCIAL PROPERTY</li>
    <li>GENERAL ELECTRICAL MAINTENANCE</li>
  </ul>

  <aside class="deals">
    <div class="deals-panel">
      <div class="deal-big">10% OFF</div>
      <div class="deal-small">ALL ELECTRICAL SERVICES</div>
      <div class="deal-or">OR</div>
      <div class="deal-big deal-free">FREE LED</div>
      <div class="deal-mid">DOWNLIGHTS<br>ON INSTALLATION</div>
      <div class="deal-terms">*Terms &amp; conditions apply</div>
    </div>
    <div class="deals-ribbon">DEALS</div>
  </aside>

  <div class="offer-ends">OFFER ENDS</div>
  <div class="offer-date"></div>
</main>
</body>
</html>
```